Business Card Design Project

I need a business card designed that is clean, simple and elegant.
I am a fashion and advertising photographer based in Cape Town and Durban South Africa.
check out my website: www.marlowvance.co.za for ideas
Updates
Hi all,
Thanks for your submissions so far!
Please note:
I want no more than than black, white and/or grey to be used.
I don't want any photos used.
I would like the card to be double sided.
I would like to continue the design similar to the past ones Ive used.
I hope this helps, please send me further questions should you have any.
many thanks!
Marlow
Hi,
Please have a look at the jpg I loaded(called inspiration) which is the direction or inspiration I am aiming at.
Also PLEASE remember NO PHOTOS to be included on the card
many thanks!!
Target Market(s)
You can look at my site to get a better understanding of the audience:
www.marlowvance.co.za
Industry/Entity Type
Advertising
Requirements
Must have
- Clean design which can also be used for a watermark on photographs
perhaps black background with white text/grey
company called: Marlow Vance Photography
Nice to have
- below I have added logos that I have used in the past.
Should not have
- pictures of cameras
tacky elements

```html
<!DOCTYPE html>
<html lang="en">
<head>
<meta charset="utf-8">
<title>Marlow Vance Photography – Business Card</title>
<link rel="stylesheet" href="https://fonts.googleapis.com/css2?family=Comfortaa:wght@600;700&display=swap">
<style>
  :root {
    --page-bg: #ffffff;
    --card-bg: #000000;
    --ink: #ffffff;
    --accent: #4fc9f5;
  }
  html, body {
    margin: 0;
    padding: 0;
    width: 1200px;
    height: 667px;
    overflow: hidden;
    background: var(--page-bg);
  }
  .canvas {
    position: relative;
    width: 1200px;
    height: 667px;
  }
  .card {
    position: absolute;
    left: 27px;
    top: 34px;
    width: 1147px;
    height: 593px;
    background: var(--card-bg);
    border-radius: 52px;
  }
  .brand-dot {
    position: absolute;
    left: 143px;
    top: 219px;
    width: 155px;
    height: 155px;
    border-radius: 50%;
    background: var(--accent);
  }
  .contact-list {
    position: absolute;
    left: 451px;
    top: 0;
    margin: 0;
    padding: 0;
    list-style: none;
    font-family: "Comfortaa", sans-serif;
    font-weight: 700;
    color: var(--ink);
    font-size: 31px;
    letter-spacing: 0.2px;
  }
  .contact-item {
    position: absolute;
    left: 0;
    display: flex;
    align-items: center;
    white-space: nowrap;
    height: 40px;
  }
  .contact-item--email  { top: 145px; }
  .contact-item--web    { top: 229px; }
  .contact-item--mobile { top: 314px; }
  .contact-item--phone  { top: 399px; }
  .contact-icon {
    width: 36px;
    height: 28px;
    flex: none;
    fill: none;
    stroke: var(--ink);
    stroke-width: 2;
  }
  .contact-text { margin-left: 38px; }
  .contact-item--web .contact-text { margin-left: 36px; }
  .contact-item--mobile .contact-text,
  .contact-item--phone .contact-text { margin-left: 40px; }
</style>
</head>
<body>
<div class="canvas">
  <div class="card">
    <div class="brand-dot"></div>
    <ul class="contact-list">
      <li class="contact-item contact-item--email">
        <svg class="contact-icon" viewBox="0 0 36 28" aria-hidden="true">
          <rect x="2" y="3" width="32" height="22"/>
          <path d="M10 15h10c0-5-3-7-6-7s-6 3-6 7 3 7 7 7"/>
          <path d="M22 19l8-8M25 11h5v5"/>
        </svg>
        <span class="contact-text">marlow@marlowvance.co.za</span>
      </li>
      <li class="contact-item contact-item--web">
        <svg class="contact-icon" viewBox="0 0 36 28" aria-hidden="true">
          <rect x="2" y="3" width="32" height="22"/>
          <path d="M6 9l2 10 3-7 3 7 2-10M20 9v10h5M20 14h4M28 9v10"/>
        </svg>
        <span class="contact-text">http://www.marlowvance.co.za</span>
      </li>
      <li class="contact-item contact-item--mobile">
        <svg class="contact-icon" viewBox="0 0 36 28" aria-hidden="true">
          <rect x="12" y="5" width="11" height="20" rx="2" transform="rotate(12 17 15)"/>
          <path d="M19 5l2-4"/>
        </svg>
        <span class="contact-text">+27 (0)82 555 0147</span>
      </li>
      <li class="contact-item contact-item--phone">
        <svg class="contact-icon" viewBox="0 0 36 28" aria-hidden="true">
          <path d="M4 11c2-6 26-6 28 0l-5 2-2-3H11l-2 3z"/>
          <rect x="8" y="13" width="20" height="11" rx="3"/>
          <circle cx="18" cy="18.5" r="3"/>
        </svg>
        <span class="contact-text">+27 (0)31 555 0862</span>
      </li>
    </ul>
  </div>
</div>
</body>
</html>
```